Ridgecrest Ag, LLC
Business cards, letterhead, envelopes
Project: Ridgecrest Ag, LLC
Ridgecrest Ag, LLC - Consulting
Creative Brief
Professional
Warren Colbeck
P.O. Box 517 Monterey, CA 93940
warren@ridgecrestag-example.com
1. I want to use my logo and will upload it. 2. I like clean, uncluttered design. 3. OK to think a little out of the box. 4. May be OK to use a different font than logo. 5. May be OK to use tagline "same dirt - new rules" differently (i.e., not right under Ridgecrest Ag as shown in logo).

```html
<!DOCTYPE html>
<html lang="en">
<head>
<meta charset="utf-8">
<title>Ridgecrest Ag, LLC – Business Card</title>
<link href="https://fonts.googleapis.com/css2?family=Open+Sans:wght@400;600;700&display=swap" rel="stylesheet">
<style>
  :root {
    --backdrop: #e9e4dc;
    --card-white: #ffffff;
    --maroon: #5a0b16;
    --gold: #f2b233;
    --text-light: #ffffff;
    --brand: #6a0f1c;
  }
  html, body {
    margin: 0;
    padding: 0;
    width: 1200px;
    height: 965px;
    overflow: hidden;
    background: var(--backdrop);
    font-family: "Open Sans", Arial, sans-serif;
  }
  .business-card {
    position: absolute;
    left: 240px;
    top: 230px;
    width: 780px;
    height: 445px;
    border-radius: 20px;
    overflow: hidden;
    background: var(--card-white);
    box-shadow: 0 6px 18px rgba(0,0,0,0.18);
  }
  .card-shapes {
    position: absolute;
    inset: 0;
  }
  .brand-name {
    position: absolute;
    left: 20px;
    top: 196px;
    width: 400px;
    text-align: center;
    margin: 0;
    font-size: 44px;
    line-height: 60px;
    font-weight: 600;
    letter-spacing: 1px;
    color: var(--brand);
  }
  .holder-name {
    position: absolute;
    right: 24px;
    top: 20px;
    margin: 0;
    font-size: 30px;
    line-height: 44px;
    font-weight: 700;
    color: var(--text-light);
  }
  .contact-list {
    position: absolute;
    right: 22px;
    top: 240px;
    margin: 0;
    padding: 0;
    list-style: none;
    text-align: right;
    color: var(--text-light);
    font-size: 16px;
    line-height: 29px;
    letter-spacing: -0.1px;
  }
  .contact-list li {
    display: flex;
    justify-content: flex-end;
    align-items: center;
    gap: 7px;
    height: 29px;
  }
  .contact-icon {
    width: 17px;
    height: 17px;
    flex: none;
  }
  .icon-spacer { width: 17px; flex: none; }
</style>
</head>
<body>
  <article class="business-card">
    <svg class="card-shapes" viewBox="0 0 780 445" width="780" height="445" aria-hidden="true">
      <path d="M400 0 C450 110 458 330 408 445 L780 445 L780 0 Z" fill="var(--gold)"/>
      <path d="M413 0 C465 110 474 330 434 445 L780 445 L780 0 Z" fill="var(--maroon)"/>
    </svg>

    <h1 class="brand-name">Ridgecrest Ag</h1>

    <h2 class="holder-name">Warren Colbeck</h2>

    <ul class="contact-list">
      <li>P.O. Box 517<span class="icon-spacer"></span></li>
      <li>Monterey, CA 93940<span class="icon-spacer"></span></li>
      <li>(831) 555-0148
        <svg class="contact-icon" viewBox="0 0 18 18" aria-label="mobile"><rect x="5" y="1" width="8" height="16" rx="1.5" fill="none" stroke="#fff" stroke-width="1.6"/><rect x="6.8" y="3.5" width="4.4" height="7" fill="#fff"/></svg>
      </li>
      <li>(831) 555-0193
        <svg class="contact-icon" viewBox="0 0 18 18" aria-label="fax"><rect x="4" y="2" width="10" height="5" fill="#fff"/><rect x="1" y="7" width="16" height="8" rx="1.5" fill="#fff"/><rect x="4" y="10" width="10" height="2" fill="var(--maroon)"/></svg>
      </li>
      <li>warren@ridgecrestag-example.com
        <svg class="contact-icon" viewBox="0 0 18 18" aria-label="email"><text x="9" y="14" text-anchor="middle" font-size="15" font-weight="700" fill="#fff" font-family="Open Sans, sans-serif">@</text></svg>
      </li>
      <li>www.ridgecrestag-example.com
        <svg class="contact-icon" viewBox="0 0 18 18" aria-label="website"><circle cx="9" cy="9" r="7.2" fill="none" stroke="#fff" stroke-width="1.5"/><ellipse cx="9" cy="9" rx="3.2" ry="7.2" fill="none" stroke="#fff" stroke-width="1.2"/><line x1="1.8" y1="9" x2="16.2" y2="9" stroke="#fff" stroke-width="1.2"/></svg>
      </li>
    </ul>
  </article>
</body>
</html>
```